Coral Bay Dental Surgery Business Cards

Hi there

Can i please have a simple business card designed (front and back with a black background) using out white reverse logo and the same font used for the logo?
On the back we can just have the logo. Full details at the front part.
Here are the details:

Name of the surgery: Coral Bay | Dental Surgery
Name on the business card: Dr Owen Thackery
Credentials:
BDSc (KTL)
MSc Oral Implantology (Halvorsen, Frankfurt)
Fellow & Diplomate (Meridian Council of Restorative Prosthetics)

Email: owen.thackery@coralbaysmile.example
Address: 17 Lisgrove Rd Karrinyup
Website: coralbaysmile.example
Phone: 1800 316 482

We have attached our high res logo and a rudimentary version of the business card which is not necessarily what we want but gives all the details
We would like to have the print ready version. Thanks.

Contact Information for Business Card

website. credentials. qr code. address. phone number

Requirements
Must have
• QR code

```html
<!DOCTYPE html>
<html lang="en">
<head>
<meta charset="utf-8">
<title>Coral Bay Dental Surgery – Business Cards</title>
<link rel="stylesheet" href="https://fonts.googleapis.com/css2?family=Montserrat:wght@400;500;700&display=swap">
<style>
  :root {
    --stage: #2a2a2c;
    --card: #141414;
    --ink: #ffffff;
    --ink-soft: #d9d9d9;
    --qr-field: #f2f2f2;
  }
  * { box-sizing: border-box; margin: 0; padding: 0; }
  html, body {
    width: 1200px; height: 900px; overflow: hidden;
    background: var(--stage);
    font-family: "Montserrat", Arial, sans-serif;
    color: var(--ink);
  }
  .sheet { position: relative; width: 1200px; height: 900px; }
  .card {
    position: absolute;
    width: 560px; height: 320px;
    background: var(--card);
    border-radius: 4px;
    box-shadow: 0 14px 36px rgba(0,0,0,.55);
    overflow: hidden;
  }
  .card--details { left: 560px; top: 90px; }
  .card--brand { left: 80px; top: 470px; }

  .details { position: absolute; left: 40px; top: 36px; width: 360px; }
  .details__name { font-size: 25px; font-weight: 700; letter-spacing: .2px; margin-bottom: 10px; }
  .details__creds { font-size: 12px; line-height: 1.35; color: var(--ink-soft); font-weight: 400; }
  .details__dash { width: 14px; height: 2px; background: var(--ink); margin: 34px 0 10px; }
  .contact { list-style: none; font-size: 12.5px; line-height: 1.45; font-weight: 500; white-space: nowrap; }
  .contact__key { display: inline-block; width: 22px; }

  .qr {
    position: absolute; right: 36px; bottom: 36px;
    width: 96px; height: 96px;
    background: var(--qr-field);
    border-radius: 3px;
  }

  .brand {
    position: absolute; inset: 0;
    display: flex; align-items: center; justify-content: center; gap: 16px;
  }
  .brand__dot { width: 22px; height: 22px; border-radius: 50%; background: var(--ink); }
  .brand__name { font-size: 26px; font-weight: 500; letter-spacing: 1px; color: var(--ink); }
</style>
</head>
<body>
<main class="sheet">
  <section class="card card--details" aria-label="Card front with contact details">
    <div class="details">
      <h1 class="details__name">Dr Owen Thackery</h1>
      <p class="details__creds">
        BDSc (KTL)<br>
        MSc Oral Implantology (Halvorsen, Frankfurt)<br>
        Fellow &amp; Diplomate<br>
        (Meridian Council of Restorative Prosthetics)
      </p>
      <div class="details__dash"></div>
      <ul class="contact">
        <li><span class="contact__key">T</span>: 1800 316 482</li>
        <li><span class="contact__key">W</span>: www.coralbaysmile.example</li>
        <li><span class="contact__key">E</span>: owen.thackery@coralbaysmile.example</li>
        <li><span class="contact__key">A</span>: 17 Lisgrove Rd Karrinyup</li>
      </ul>
    </div>
    <div class="qr" role="img" aria-label="QR code area linking to www.coralbaysmile.example"></div>
  </section>

  <section class="card card--brand" aria-label="Card back with practice name">
    <div class="brand">
      <span class="brand__dot"></span>
      <span class="brand__name">Coral Bay | Dental Surgery</span>
    </div>
  </section>
</main>
</body>
</html>
```